Letterhead design for Sleep Consulting Business

I'm looking for a new letterhead (heading/footer) design for my Sleep Consulting Business, I work with families to help their children improve their sleep.

The heading/footer will used in Microsoft Word Only-to be used for all of my documents such as writing Sleep Plans. I need to utilize as much working space in the document as possible. This will NOT be printed out on paper- it will only be used for heading/footer on microsoft word, then emailed to clients, who may print it at home.

My brand colors:
Dark Blue Hex: 1F2A42
Lighter Blueish Hex: 90BEC9
You're welcome to check out my website for inspiration- it is freshly created with other colors as well, and I love the outcome. www.hollowpinerest.com

Target Market(s)

Tired parents

Font styles to use
Script
Other font styles liked:
• Great Vibe, Lato or Just Another Hand are all used currently for my brand. Open to other options.

Requirements
Must have
• The letterhead (heading/footer) MUST be kept narrow (height-wise), so I have plenty of space on my document, while including important information.

It should look professional on screen, and when printed.

Must include my business name OR logo (Hollow Pine Sleep Consulting), and my email address. Mara@hollowpinerest.com

Website is optional, not required, just if you need to fill in a spot: www.hollowpinerest.com

```html
<!DOCTYPE html>
<html lang="en">
<head>
<meta charset="utf-8">
<title>Hollow Pine Sleep Consulting – Letterhead</title>
<link rel="stylesheet" href="https://fonts.googleapis.com/css2?family=Lato:wght@400;700&family=Open+Sans:wght@400;600;700&display=swap">
<style>
  :root {
    --navy: #1F2A42;
    --sky: #90BEC9;
    --paper: #fafafa;
    --stage: #ececec;
    --ink: #555a60;
    --ink-dark: #3d4148;
  }
  * { box-sizing: border-box; margin: 0; padding: 0; }
  html, body { width: 1100px; height: 1200px; overflow: hidden; background: var(--stage); }
  .letterhead {
    position: absolute; left: 126px; top: 0;
    width: 848px; height: 1200px;
    background: var(--paper);
    overflow: hidden;
    font-family: "Open Sans", Arial, sans-serif;
    color: var(--ink);
  }
  .header-band { position: absolute; left: 0; top: 0; width: 848px; height: 40px; }
  .footer-band { position: absolute; left: 0; bottom: 0; width: 848px; height: 90px; }
  .brand { position: absolute; left: 60px; top: 76px; display: flex; align-items: center; gap: 16px; }
  .brand-mark { width: 84px; height: 84px; border-radius: 50%; background: var(--navy); flex: none; }
  .brand-name {
    font-family: "Lato", Arial, sans-serif; font-weight: 700;
    font-size: 24px; line-height: 1.25; color: var(--navy); letter-spacing: 0.3px;
  }
  .contact {
    position: absolute; right: 61px; top: 102px;
    font-family: "Lato", Arial, sans-serif; font-size: 15.5px; color: var(--navy);
    text-align: right; list-style: none;
  }
  .contact li { display: flex; align-items: center; justify-content: flex-end; gap: 10px; height: 19px; }
  .contact svg { width: 13px; height: 13px; }
  .letter { position: absolute; left: 61px; top: 228px; width: 720px; font-size: 12.5px; line-height: 21.5px; }
  .salutation { margin-left: 26px; margin-bottom: 43px; }
  .letter p.body { text-indent: 26px; text-align: justify; margin-bottom: 21.5px; }
  .sign-off { position: absolute; left: 87px; top: 698px; font-size: 12.5px; }
  .sign-name { font-weight: 700; color: var(--ink-dark); }
  .signature {
    display: block; width: 180px; height: 56px; margin: 4px 0 12px -22px;
    border-radius: 6px; background: linear-gradient(90deg, rgba(31,42,66,0.12), rgba(31,42,66,0.04));
  }
  .follow {
    position: absolute; left: 660px; top: 1160px; display: flex; align-items: center; gap: 8px;
    font-family: "Lato", Arial, sans-serif; font-size: 14.5px; color: #fff;
  }
  .social-dot { width: 17px; height: 17px; border-radius: 50%; border: 1.5px solid var(--sky); }
</style>
</head>
<body>
<main class="letterhead">
  <svg class="header-band" viewBox="0 0 848 40" preserveAspectRatio="none" aria-hidden="true">
    <rect x="0" y="0" width="848" height="22" fill="var(--navy)"/>
    <rect x="0" y="27" width="848" height="5" fill="var(--sky)"/>
  </svg>

  <div class="brand">
    <span class="brand-mark"></span>
    <div class="brand-name">Hollow Pine<br>Sleep Consulting</div>
  </div>

  <ul class="contact">
    <li>555-301-7284
      <svg viewBox="0 0 14 14"><circle cx="7" cy="7" r="6" fill="none" stroke="var(--sky)" stroke-width="1.2"/><path d="M4.8,4.2 L6,4 L6.6,5.6 L5.9,6.2 C6.3,7.1 6.9,7.7 7.8,8.1 L8.4,7.4 L10,8 L9.8,9.2 C7.2,9.4 4.6,6.8 4.8,4.2Z" fill="var(--sky)"/></svg>
    </li>
    <li>Mara@hollowpinerest.com
      <svg viewBox="0 0 14 14"><rect x="1.5" y="3" width="11" height="8" fill="none" stroke="var(--sky)" stroke-width="1.2"/><path d="M1.5,3 L7,7.5 L12.5,3" fill="none" stroke="var(--sky)" stroke-width="1.2"/></svg>
    </li>
    <li>www.hollowpinerest.com
      <svg viewBox="0 0 14 14"><circle cx="7" cy="7" r="6" fill="none" stroke="var(--sky)" stroke-width="1.2"/><ellipse cx="7" cy="7" rx="2.6" ry="6" fill="none" stroke="var(--sky)" stroke-width="1"/><path d="M1,7 H13 M2,4 H12 M2,10 H12" stroke="var(--sky)" stroke-width="1"/></svg>
    </li>
  </ul>

  <section class="letter">
    <p class="salutation">Dear Sir,</p>
    <p class="body">Lorem Ipsum is simply dummy text of the printing and typesetting industry. Lorem Ipsum has been the industry's standard dummy text ever since the 1500s, when an unknown printer took a galley of type and scrambled it to make a type specimen book. It has survived not only five centuries, but also the leap into electronic typesetting, remaining essentially unchanged. It was popularised in the 1960s with the release of Kestrel sheets containing Lorem Ipsum passages, and more recently with desktop publishing software like Quillset Writer including versions of Lorem Ipsum.</p>
    <p class="body">Lorem Ipsum is simply dummy text of the printing and typesetting industry. Lorem Ipsum has been the industry's standard dummy text ever since the 1500s, when an unknown printer took a galley of type and scrambled it to make a type specimen book. It has survived not only five centuries, but also the leap into electronic typesetting, remaining essentially unchanged. It was popularised in the 1960s with the release of Kestrel sheets containing Lorem Ipsum passages, and more recently with desktop publishing software like Quillset Writer including versions of Lorem Ipsum.</p>
    <p class="body">Lorem Ipsum is simply dummy text of the printing and typesetting industry. Lorem Ipsum has been the industry's standard dummy text ever since the 1500s, when an unknown printer took a galley of type and scrambled it to make a type specimen book.</p>
  </section>

  <div class="sign-off">
    <p class="sign-name">Your Name</p>
    <span class="signature" role="img" aria-label="Handwritten signature of Owen Calder"></span>
    <p>CEO &nbsp;|&nbsp; Owner</p>
  </div>

  <svg class="footer-band" viewBox="0 0 848 90" preserveAspectRatio="none" aria-hidden="true">
    <rect x="0" y="22" width="848" height="5" fill="var(--sky)"/>
    <rect x="0" y="34" width="848" height="56" fill="var(--navy)"/>
  </svg>

  <div class="follow">
    <span>Follow us on:</span>
    <span class="social-dot"></span>
    <span class="social-dot"></span>
  </div>
</main>
</body>
</html>
```